Psychiatrist/ Psychotherapist needs a letterhead design

I am a Psychiatrist working in private practice. I work as a psychotherapist and treat patients with depression, anxiety, post traumatic stress and relationship problems. I need a letterhead which is elegant and professional. I would like to see designs using colours such as blues and greys.
I would like the information on the letterhead split between the top and bottom of the page to give it a look of balance.
I want it to look elegant, feminine and upmarket. I don't want it to look too corporate but to show some flair and to be a bit artistic.

Other doctors, specialists and agencies who have referred patients to me.

Work

Script

Requirements
Must have
• My name and my profession psychiatrist need to be highlighted and prominent. It needs to be professional looking and elegant without being old fashioned or too conservative.
Nice to have
• Balance between the top and bottom of the page.
Should not have
• I don't want fonts which are old and too traditional.

```html
<!DOCTYPE html>
<html lang="en">
<head>
<meta charset="utf-8">
<title>Halcyon Psychiatry Letterhead</title>
<link rel="stylesheet" href="https://fonts.googleapis.com/css2?family=Arimo:wght@400;700&family=Source+Sans+3:wght@400;600;700&display=swap">
<style>
  :root {
    --bg: #5a5a5a;
    --paper: #ffffff;
    --brand-blue: #1d63b8;
    --swoosh-grey: #9a9ca1;
    --ink: #1e1e1e;
    --muted: #555555;
    --signature-fill: #e6e8ee;
  }
  * { box-sizing: border-box; margin: 0; padding: 0; }
  html, body { width: 1200px; height: 795px; overflow: hidden; background: var(--bg); }
  .letterhead {
    position: absolute; left: 330px; top: 18px;
    width: 540px; height: 758px;
    background: var(--paper);
    font-family: "Arimo", Arial, sans-serif;
    color: var(--ink);
    overflow: hidden;
  }
  .header-swoosh { position: absolute; left: 0; top: 0; width: 540px; height: 70px; }
  .brand {
    position: absolute; left: 350px; top: 40px;
    display: flex; align-items: center; gap: 8px;
  }
  .brand-mark { width: 14px; height: 14px; background: var(--brand-blue); }
  .brand-name {
    font-family: "Source Sans 3", Arial, sans-serif;
    font-weight: 700; color: var(--brand-blue);
    font-size: 19px; line-height: 19px; letter-spacing: 1px;
  }
  .recipient {
    position: absolute; left: 44px; top: 130px;
    font-size: 10px; line-height: 12px; font-style: normal;
  }
  .recipient strong { font-weight: 700; }
  .letter-body {
    position: absolute; left: 44px; top: 190px; width: 454px;
    font-size: 9.8px; line-height: 14.2px;
  }
  .letter-body p { margin-bottom: 14.2px; }
  .letter-body p.wide-gap { margin-bottom: 28.4px; }
  .signature {
    position: absolute; left: 52px; top: 608px;
    width: 124px; height: 36px;
    background: var(--signature-fill); border-radius: 4px;
  }
  .contact-footer {
    position: absolute; left: 0; width: 540px; top: 710px;
    text-align: center; font-family: "Source Sans 3", Arial, sans-serif;
  }
  .doctor-name { color: var(--brand-blue); font-size: 10px; font-weight: 600; line-height: 13px; }
  .doctor-name small { font-size: 7.5px; color: var(--muted); font-weight: 400; }
  .phone-line { color: var(--brand-blue); font-size: 9.2px; font-weight: 700; line-height: 13px; }
  .address-line { font-family: "Arimo", Arial, sans-serif; font-size: 8.6px; line-height: 13px; color: #333; }
  .footer-band { position: absolute; left: 0; bottom: 0; width: 540px; height: 7px; background: var(--brand-blue); }
</style>
</head>
<body>
  <main class="letterhead">
    <svg class="header-swoosh" viewBox="0 0 540 70" aria-hidden="true">
      <rect x="0" y="0" width="540" height="10" fill="var(--brand-blue)"/>
      <path d="M0 10 L540 10 L540 13 C380 15 180 22 0 50 Z" fill="var(--brand-blue)"/>
      <path d="M0 50 C150 30 300 24 360 24 C260 30 120 46 0 64 Z" fill="var(--swoosh-grey)"/>
    </svg>

    <div class="brand">
      <span class="brand-mark"></span>
      <span class="brand-name">HALCYON<br>PSYCHIATRY</span>
    </div>

    <address class="recipient">
      To<br>
      <strong>Mr. Arun Mehta</strong><br>
      Executive Graphic Designer<br>
      Bright Pane Studio
    </address>

    <section class="letter-body">
      <p>Lorem Ipsum is simply dummy text of the printing and typesetting industry. Lorem Ipsum has been the industry's standard dummy text ever since the 1500s, when an unknown printer took a galley of type and scrambled it to make a type specimen book. It has survived not only five centuries, but also the leap into electronic typesetting, remaining essentially unchanged. It was popularised in the 1960s with the release of Transfertype sheets containing Lorem Ipsum passages, and more recently with desktop publishing software like LayoutPro Desk including versions of Lorem Ipsum.</p>
      <p class="wide-gap">It is a long established fact that a reader will be distracted by the readable content of a page when looking at its layout. The point of using Lorem Ipsum is that it has a more-or-less normal distribution of letters, as opposed to using 'Content here, content here', making it look like readable English. Many desktop publishing packages and web page editors now use Lorem Ipsum as their default model text, and a search for 'lorem ipsum' will uncover many web sites still in their infancy. Various versions have evolved over the years, sometimes by accident, sometimes on purpose (injected humour and the like).</p>
      <p>Contrary to popular belief, Lorem Ipsum is not simply random text. It has roots in a piece of classical Latin literature from 45 BC, making it over 2000 years old. Daniel Ashford, a Latin professor at Westbrook College in Virginia, looked up one of the more obscure Latin words, consectetur, from a Lorem Ipsum passage, Contrary to popular belief, Lorem Ipsum is not simply random text. It has roots in a piece of classical Latin literature from 45 BC, making it over 2000 years old. Daniel Ashford, a Latin professor at Westbrook College in Virginia, looked up one of the more obscure Latin words, consectetur, from and going through the cites of the word in classical literature, discovered the</p>
      <p>The standard chunk of Lorem Ipsum used since the 1500s is reproduced below for those interested. Sections 1.10.32 and 1.10.33 from "de Rebus Quietis et Turbidis" by Varenus are also reproduced in their exact original form, accompanied by English versions from the 1914 translation by J. Thornley.</p>
      <p>Thanks and Regards,</p>
    </section>

    <div class="signature" role="img" aria-label="Handwritten signature"></div>

    <footer class="contact-footer">
      <div class="doctor-name">Dr. Clara Whitfield, <small>B.Med</small></div>
      <div class="phone-line">Tel: (08) 8100 4521 | Fax: (08) 8100 4522 | Mob: 0400123987</div>
      <div class="address-line">E-mail: cwhitfield@halcyonmind.net &nbsp;| &nbsp;12 Elm Grove, Norwood, SA 5067</div>
    </footer>

    <div class="footer-band"></div>
  </main>
</body>
</html>
```